Build a Web page - Dovin Pratchell Homes, LLC - a custom home builder

We are a custom home builder in Wisconsin. Need a basic web page with a home page, About Us, Contact info, Gallery, and Testimonials page. Gallery will probably have sub-pages and each will have about ten pictures or less. I already own the domain and have web hosting through Wix, I just need the site built. Once the page is built I should be able to do the upkeep on it myself. If I need to add pictures or whatever.
Updates

Project Deadline Extended
Reason: I am still looking through designs and will select soon - thank you!

Target Market(s)

Gen X and Millennials who are looking to build a home. Custom built homes - not generic spec homes.

Industry/Entity Type

Home Builder

Number of Pages Required

5+ page

Font styles to use
Sans Serif

Colors
ffffff
ec1f27
000000
9d9d9d

Requirements
Must have
• I have no idea if I want coded or in coded. I'm not sure of the difference and why I would want one over the other.
Nice to have
• We like the following colors - red, black, gray, white.
Should not have
• not a big fan of clip art like hammers, tape measures, etc. Must look professional.

```html
<!DOCTYPE html>
<html lang="en">
<head>
<meta charset="utf-8">
<title>Dovin Pratchell Homes, LLC — Custom Home Builder</title>
<link rel="stylesheet" href="https://fonts.googleapis.com/css2?family=Mulish:wght@400;600;700&family=Open+Sans:wght@400;600&display=swap">
<style>
:root{
  --red:#ec1f27;
  --red-dark:#b3161d;
  --black:#000000;
  --white:#ffffff;
  --grey:#9d9d9d;
  --grey-light:#e6e6e6;
  --text:#333333;
  --text-soft:#6b6b6b;
  --line:#cfcfcf;
}
*{box-sizing:border-box;margin:0;padding:0}
html,body{width:1200px;height:2535px;overflow:hidden;background:var(--white)}
body{position:relative;font-family:"Open Sans",Arial,sans-serif;color:var(--text)}
.abs{position:absolute}

/* header */
.site-header{left:0;top:0;width:1200px;height:103px;background:var(--white);z-index:3}
.brand{left:118px;top:5px;width:178px;height:152px;background:var(--white);border:2px solid #bdbdbd;box-shadow:0 2px 6px rgba(0,0,0,.2);z-index:5;display:flex;flex-direction:column;align-items:center;justify-content:center;gap:12px}
.brand-square{width:44px;height:44px;background:var(--grey)}
.brand-name{font-family:"Mulish",Arial,sans-serif;font-weight:700;font-size:17px;line-height:1.2;color:var(--red-dark);text-align:center;text-transform:uppercase}
.phone{left:910px;top:14px;font-family:"Mulish",Arial,sans-serif;font-weight:700;font-size:19px;color:var(--black);display:flex;align-items:center;gap:6px}
.main-nav a{position:absolute;top:58px;font-family:"Mulish",Arial,sans-serif;font-size:16px;color:#222;text-decoration:none;letter-spacing:.3px}
.main-nav a.active{color:var(--red)}
.nav-underline{left:452px;top:97px;width:71px;height:5px;background:var(--red)}

/* hero */
.hero{left:0;top:103px;width:1200px;height:590px;background:linear-gradient(180deg,#5f86bd 0%,#9fbadb 22%,#6c7a6a 40%,#5e6a54 62%,#6e8f3d 78%,#7da23f 100%)}
.hero-curve{left:0;top:590px}
.hero-title{left:0;top:268px;width:1200px;text-align:center;font-family:"Mulish",Arial,sans-serif;font-weight:700;font-size:50px;color:var(--white);letter-spacing:1px;text-shadow:0 2px 6px rgba(0,0,0,.35)}
.hero-sub{left:0;top:328px;width:1200px;text-align:center;font-family:"Mulish",Arial,sans-serif;font-weight:700;font-size:33px;color:var(--white);letter-spacing:1px;text-shadow:0 2px 6px rgba(0,0,0,.35)}
.btn-quote{left:495px;top:394px;width:208px;height:46px;border:2px solid var(--white);color:var(--white);font-family:"Mulish",Arial,sans-serif;font-weight:700;font-size:18px;display:flex;align-items:center;justify-content:center}
.slider-dots{left:516px;top:591px;display:flex;gap:8px}
.slider-dots span{width:32px;height:4px;background:var(--white)}
.slider-dots span.current{background:#e4d62b}

/* welcome */
.welcome-hex{left:132px;top:671px}
.welcome-title{left:488px;top:716px;font-family:"Mulish",Arial,sans-serif;font-size:30px;color:#333;letter-spacing:.5px}
.welcome-text{left:493px;top:775px;width:590px;font-size:14.5px;line-height:23px;color:var(--text-soft)}
.welcome-text p+p{margin-top:14px}
.btn-red{left:495px;top:977px;width:162px;height:42px;background:var(--red);color:var(--white);font-family:"Mulish",Arial,sans-serif;font-weight:600;font-size:16px;display:flex;align-items:center;justify-content:center}

/* services */
.services{left:0;top:1102px;width:1200px;height:389px;background:linear-gradient(90deg,#cfcfcf,#dadada 50%,#cbcbcb)}
.service-card{top:1166px;width:474px;height:288px;background:var(--white);box-shadow:0 1px 4px rgba(0,0,0,.25)}
.service-card svg{position:absolute;left:0;top:0}
.service-title{position:absolute;left:27px;top:46px;font-family:"Mulish",Arial,sans-serif;font-size:25px}
.service-text{position:absolute;left:27px;top:84px;width:178px;font-size:13px;line-height:20px;color:var(--text-soft)}
.service-text p+p{margin-top:12px}
.btn-outline{position:absolute;left:27px;top:214px;width:136px;height:36px;border:2px solid;font-family:"Mulish",Arial,sans-serif;font-size:14px;display:flex;align-items:center;justify-content:center}
.card-what .service-title,.card-what .btn-outline{color:var(--red-dark);border-color:var(--red)}
.card-how .service-title{color:#444}
.card-how .btn-outline{color:#222;border-color:#444}

/* gallery */
.gallery{left:0;top:1491px;width:1200px;height:475px;background:var(--red)}
.gallery-title{left:0;top:1516px;width:1200px;text-align:center;font-family:"Mulish",Arial,sans-serif;font-size:29px;color:var(--white)}
.tile{border:3px solid var(--white)}

/* testimonials */
.testi-title{left:0;top:2016px;width:1200px;text-align:center;font-family:"Mulish",Arial,sans-serif;font-size:30px;color:#333}
.testi-card{top:2097px;width:421px;height:196px;border:2px solid var(--line);background:var(--white);text-align:center}
.testi-quote{position:absolute;left:0;top:50px;width:100%;font-family:Georgia,serif;font-size:48px;line-height:40px;color:#c8c8c8}
.testi-text{position:absolute;left:40px;top:82px;width:337px;font-size:14.5px;line-height:23px;color:var(--text-soft)}
.testi-author{position:absolute;left:0;top:142px;width:100%;font-size:15px;color:#222}
.avatar{top:2056px;width:80px;height:80px;border-radius:50%;border:3px solid var(--white);box-shadow:0 0 0 1px #ddd}
.arrow{top:2175px}

/* footer */
.site-footer{left:0;top:2378px;width:1200px;height:157px;background:var(--black)}
.footer-nav a{position:absolute;top:2418px;font-family:"Mulish",Arial,sans-serif;font-size:16px;color:var(--white);text-decoration:none}
.copyright{left:123px;top:2453px;font-size:13px;color:#8a8a8a}
.social{top:2411px;width:34px;height:34px;border:2px solid var(--white);border-radius:50%}
</style>
</head>
<body>

<header class="abs site-header">
  <div class="abs phone">
    <svg width="18" height="18" viewBox="0 0 24 24"><path fill="#ec1f27" d="M6.6 10.8a15.2 15.2 0 0 0 6.6 6.6l2.2-2.2c.3-.3.7-.4 1-.2 1.1.4 2.3.6 3.6.6.6 0 1 .4 1 1V20c0 .6-.4 1-1 1A17 17 0 0 1 3 4c0-.6.4-1 1-1h3.5c.6 0 1 .4 1 1 0 1.3.2 2.5.6 3.6.1.3 0 .7-.2 1z"/></svg>
    (685) 555 0172
  </div>
  <nav class="main-nav">
    <a class="active" style="left:464px">HOME</a>
    <a style="left:558px">ABOUT US</a>
    <a style="left:686px">GALLERY</a>
    <a style="left:803px">TESTIMONIALS</a>
    <a style="left:966px">CONTACT US</a>
  </nav>
  <div class="abs nav-underline"></div>
</header>

<div class="abs brand">
  <div class="brand-square"></div>
  <div class="brand-name">Dovin Pratchell<br>Homes</div>
</div>

<section>
  <div class="abs hero" role="img" aria-label="Two-storey green-sided custom home with stone accents, triple garage and lawn under a blue sky"></div>
  <svg class="abs hero-curve" width="1200" height="104" viewBox="0 0 1200 104"><path d="M0 104 L0 103 Q600 -30 1200 103 L1200 104 Z" fill="#ffffff"/></svg>
  <h1 class="abs hero-title">WE ARE A CUSTOM HOME BUILDER</h1>
  <div class="abs hero-sub">CURABITUR VEL MIAMET MAGNA</div>
  <div class="abs btn-quote">GET A QUOTE</div>
  <div class="abs slider-dots"><span></span><span></span><span class="current"></span><span></span></div>
</section>

<section>
  <svg class="abs welcome-hex" width="345" height="394" viewBox="0 0 345 394">
    <defs><linearGradient id="kitchenTone" x1="0" y1="0" x2="0" y2="1"><stop offset="0" stop-color="#cfc6bb"/><stop offset=".45" stop-color="#6e3f26"/><stop offset="1" stop-color="#3b2318"/></linearGradient></defs>
    <polygon points="172,0 345,98 345,296 172,394 0,296 0,98" fill="#ececec"/>
    <polygon points="172,22 325,110 325,284 172,372 20,284 20,110" fill="url(#kitchenTone)" role="img" aria-label="Kitchen with dark wood cabinets, island and bar stools"/>
  </svg>
  <h2 class="abs welcome-title">WELCOME TO OUR WEBSITE</h2>
  <div class="abs welcome-text">
    <p>Fusce ultricies orci ac feugiat suscipit leo massa sodales velit et scelerisque mi tortor at ipsum cligula augue bibendum accumsan vestibulum ut commodo a mi Morbi ornare gravida elit Integer congue</p>
    <p>augue et malesuada iaculis ipsum dui aliquet felis at cursus magna nisl nec elit Praesent elementum elit at tellus nec ultricies sit amet porttitor mattis enim In massa libero interdum nec interdum vel blandit sed nulla In ullamcorper est eget tempor cursus neque mi consectetuer mi a ultricies massa</p>
  </div>
  <div class="abs btn-red">READ MORE</div>
</section>

<section>
  <div class="abs services" role="img" aria-label="Faded light grey interior background"></div>
  <article class="abs service-card card-what" style="left:125px">
    <svg width="474" height="288" viewBox="0 0 474 288"><defs><linearGradient id="yardTone" x1="0" y1="0" x2="0" y2="1"><stop offset="0" stop-color="#dfe6ee"/><stop offset=".5" stop-color="#b8a58e"/><stop offset="1" stop-color="#4f8a2e"/></linearGradient></defs>
      <polygon points="186,0 474,0 474,288 296,288" fill="url(#yardTone)" role="img" aria-label="House with stone patio and fire pit on a lawn"/></svg>
    <h3 class="service-title">What We Do</h3>
    <div class="service-text"><p>facilisis volutpat in imperdiet sit amet sem Aliquam</p><p>nec erat at purus cursus interdum Vestibulum ligula augue bibendum accum</p></div>
    <div class="btn-outline">READ MORE</div>
  </article>
  <article class="abs service-card card-how" style="left:615px">
    <svg width="474" height="288" viewBox="0 0 474 288"><defs><linearGradient id="barTone" x1="0" y1="0" x2="0" y2="1"><stop offset="0" stop-color="#b06a34"/><stop offset=".5" stop-color="#8a4b26"/><stop offset="1" stop-color="#7a6e62"/></linearGradient></defs>
      <polygon points="186,0 474,0 474,288 296,288" fill="url(#barTone)" role="img" aria-label="Kitchen breakfast bar with wooden stools"/></svg>
    <h3 class="service-title">How We Work</h3>
    <div class="service-text"><p>facilisis volutpat in imperdiet sit amet sem Aliquam</p><p>nec erat at purus cursus interdum Vestibulum ligula augue bibendum accum</p></div>
    <div class="btn-outline">READ MORE</div>
  </article>
</section>

<section>
  <div class="abs gallery"></div>
  <h2 class="abs gallery-title">OUR GALLERY</h2>
  <div class="abs tile" style="left:128px;top:1584px;width:359px;height:317px;background:linear-gradient(180deg,#3f6fc0 0%,#8fb0dc 35%,#5f6b55 55%,#4f8a2a 75%,#5c9a30 100%)" role="img" aria-label="Rear view of a green two-storey home on a lawn"></div>
  <div class="abs tile" style="left:500px;top:1584px;width:184px;height:152px;background:linear-gradient(180deg,#cdbfa8,#9a6a3e)" role="img" aria-label="Built-in wooden cabinet and shelves"></div>
  <div class="abs tile" style="left:696px;top:1584px;width:377px;height:152px;background:linear-gradient(180deg,#d9d2c6,#a22a2a 60%,#4a2c20)" role="img" aria-label="Bedroom with red patterned bedspread"></div>
  <div class="abs tile" style="left:500px;top:1749px;width:184px;height:152px;background:linear-gradient(135deg,#8c8a86,#5d5b58)" role="img" aria-label="Slate tile floor detail"></div>
  <div class="abs tile" style="left:696px;top:1749px;width:171px;height:152px;background:linear-gradient(180deg,#d8cf9e,#b59b63 60%,#efeee8)" role="img" aria-label="Bathroom with white vanity"></div>
  <div class="abs tile" style="left:879px;top:1749px;width:194px;height:152px;background:linear-gradient(180deg,#6b4a34,#cbb99f 60%,#7a5636)" role="img" aria-label="Laundry room with wood cabinets"></div>
</section>

<section>
  <h2 class="abs testi-title">TESTIMONIALS</h2>
  <svg class="abs arrow" style="left:118px" width="22" height="38" viewBox="0 0 22 38"><path d="M19 3 L4 19 L19 35" fill="none" stroke="#b5b5b5" stroke-width="4"/></svg>
  <svg class="abs arrow" style="left:1044px" width="22" height="38" viewBox="0 0 22 38"><path d="M3 3 L18 19 L3 35" fill="none" stroke="#b5b5b5" stroke-width="4"/></svg>
  <blockquote class="abs testi-card" style="left:167px">
    <div class="testi-quote">&ldquo;</div>
    <p class="testi-text">inceptos hymenaeos Proin nulla arcu nonummy luctus dictum eget fermentum et lorem</p>
    <p class="testi-author">By Author Name</p>
  </blockquote>
  <blockquote class="abs testi-card" style="left:605px">
    <div class="testi-quote">&ldquo;</div>
    <p class="testi-text">inceptos hymenaeos Proin nulla arcu nonummy luctus dictum eget fermentum et lorem</p>
    <p class="testi-author">By Author Name</p>
  </blockquote>
  <div class="abs avatar" style="left:335px;background:linear-gradient(180deg,#8a7a6a,#c9a58c)" role="img" aria-label="Client portrait"></div>
  <div class="abs avatar" style="left:775px;background:linear-gradient(180deg,#4a4f57,#2a2e35)" role="img" aria-label="Client portrait"></div>
</section>

<footer class="abs site-footer"></footer>
<nav class="footer-nav">
  <a style="left:123px">HOME</a>
  <a style="left:208px">ABOUT US</a>
  <a style="left:328px">GALLERY</a>
  <a style="left:436px">TESTIMONIALS</a>
  <a style="left:590px">CONTACT US</a>
</nav>
<div class="abs copyright">© 2017 Company Name &nbsp;All right reserved &nbsp;Term of Use</div>
<div class="abs social" style="left:919px"></div>
<div class="abs social" style="left:960px"></div>
<div class="abs social" style="left:1000px"></div>
<div class="abs social" style="left:1041px"></div>

</body>
</html>
```